TQRVA Membership Flyer

• 1 Page Flyer promoting TQRVA Membership Drive
• I have attached our organization brochure for organizational info
• Please include the same TQRVA logo as seen in brochure
• Membership $20/year
• Contact Milo Banter to Join at banmil42@learners.fpx.edu
INCLUDE Organization Advisers
Dr. Torvald Penning FPX School of Dental Medicine (photo from attached brochure)
Dr. Felix Ormond FPX Talwick School of Medicine (Photo from Attached brochure)

Member Benefits
• Access to exclusive Interdisciplinary world-renowned guest speaker presentations
• Mentorship for residencies / Oral Medicine Fellowship for nondental healthcare students
• Shadowing opportunities with Oral Medicine Specialist
• Participate in research journal club
• Clinical Research, Case Reports and Lindqvart Fellowship opportunities
• Exclusive Lunch and Learn Invitations
• 10% Discount to Special Events Sponsored by TQRVA
• Enhance your Interdisciplinary resource network

Renew or Join TQRVA by August 30th and be entered in a free raffle for the chance to win one of 3 drawings
$50 Pavex Gift Card
2x $25 Brewmoor Gift Card

Target Market(s)

Students

Requirements
Must have
• Must use the TQRVA Logo from brochure, Member Benefits • Access to exclusive Interdisciplinary world-renowned guest speaker presentations • Mentorship for residencies / Oral Medicine Fellowship for nondental healthcare students • Shadowing opportunities with Oral Medicine Specialist • Participate in research journal club • Clinical Research, Case Reports and Lindqvart Fellowship opportunities • Exclusive Lunch and Learn Invitations • 10% Discount to Special Events Sponsored by TQRVA • Enhance your Interdisciplinary resource network Renew or Join TQRVA by August 30th and be entered in a free raffle for the chance to win one of 3-4 drawings $50 Pavex Gift Card 2x $25 Brewmoor Gift Card
Nice to have
• Similar design background to brochure attached,

```html
<!DOCTYPE html>
<html lang="en">
<head>
<meta charset="utf-8">
<title>TQRVA Membership Flyer</title>
<link rel="stylesheet" href="https://fonts.googleapis.com/css2?family=Montserrat:wght@500;600;700;800&family=Oswald:wght@400;500;700&family=Libre+Baskerville:wght@400&display=swap">
<style>
  :root{
    --purple:#4b1a8a;
    --purple-light:#6a3aa6;
    --gold:#c9a93f;
    --gold-soft:#e3cf8a;
    --ink:#2f2f35;
    --slate:#4a4a4f;
    --paper:#f5f5f7;
    --green:#1f6b2a;
  }
  *{margin:0;padding:0;box-sizing:border-box}
  html,body{width:990px;height:1200px;overflow:hidden}
  body{position:relative;background:var(--paper);font-family:"Montserrat",sans-serif;color:var(--ink)}
  .abs{position:absolute}
  .top-white{left:0;top:0;width:990px;height:600px;background:#fff}

  .brand{left:60px;top:70px;width:300px;text-align:center}
  .brand-name{font-family:"Montserrat",sans-serif;font-weight:800;color:var(--purple);font-size:60px;line-height:64px;letter-spacing:1px}
  .brand-tagline{margin-top:8px;font-family:"Libre Baskerville",serif;color:var(--gold);font-size:10.5px;white-space:nowrap}

  .hero-art{left:0;top:0}

  .badge-title{left:63px;top:326px;width:412px;height:76px;text-align:center;font-family:"Oswald",sans-serif;font-weight:700;color:#fff;font-size:62px;line-height:76px;letter-spacing:1px}
  .badge-price{left:76px;top:404px;width:386px;text-align:center;font-family:"Oswald",sans-serif;font-weight:700;color:var(--gold);font-size:108px;line-height:116px}
  .badge-term{left:76px;top:522px;width:386px;text-align:center;font-family:"Oswald",sans-serif;font-weight:400;color:var(--gold);font-size:32px;letter-spacing:5px}

  .benefits-head{left:66px;top:612px;width:431px;height:50px;background:var(--purple);color:#fff;font-weight:800;font-size:31px;line-height:50px;padding-left:32px;letter-spacing:.5px}
  .benefits-head span{color:var(--gold)}
  .benefits{left:82px;top:682px;width:465px;list-style:none}
  .benefits li{position:relative;padding-left:18px;font-size:14.4px;font-weight:500;line-height:19px;margin-bottom:8px;color:var(--ink)}
  .benefits li svg{position:absolute;left:0;top:3px;width:13px;height:13px}

  .advisers-head{left:576px;top:609px;width:346px;height:35px;background:var(--gold);color:#fff;font-weight:700;font-size:19.5px;line-height:35px;text-align:center;letter-spacing:.5px}
  .portrait{left:576px;width:127px;height:140px;border:5px solid var(--gold-soft);background:linear-gradient(180deg,#6e6e74,#b9bac0)}
  .portrait.one{top:652px}
  .portrait.two{top:802px;background:linear-gradient(180deg,#5f6066,#c5c8d0)}
  .adviser{left:723px;width:200px}
  .adviser.one{top:684px}
  .adviser.two{top:833px}
  .adviser-name{font-weight:700;color:var(--purple);font-size:16.5px;padding-bottom:6px;border-bottom:1px solid var(--purple)}
  .adviser-school{margin-top:8px;font-weight:600;color:var(--slate);font-size:16.5px;line-height:22px}

  .raffle{left:66px;top:959px;width:858px;height:151px;border:1.5px solid var(--gold-soft);border-radius:6px;background:rgba(255,255,255,.85)}
  .raffle-title{left:92px;top:980px;width:319px;font-weight:800;color:var(--purple);font-size:32px;line-height:32px;letter-spacing:.5px;white-space:nowrap}
  .raffle-deadline{left:94px;top:1016px;width:315px;height:31px;background:var(--gold);color:#fff;font-weight:700;font-size:19.5px;line-height:31px;text-align:center}
  .raffle-note{left:94px;top:1056px;font-weight:600;color:var(--slate);font-size:13.8px;line-height:19px}
  .prize{top:980px;width:208px;height:109px;background:linear-gradient(180deg,#f1f1f3,#e2e2e6);border-radius:4px}
  .prize.one{left:448px}
  .prize.two{left:688px}
  .bow{position:absolute;left:0;top:-6px;width:76px;height:70px;border-radius:6px;background:radial-gradient(circle at 45% 45%,#f2dc85,#b89322)}
  .prize-amount{position:absolute;font-weight:800;color:var(--purple)}
  .prize.one .prize-amount{left:86px;top:10px;font-size:52px;line-height:60px}
  .prize.one .prize-label{position:absolute;left:16px;top:76px;font-weight:800;font-size:19px;color:var(--gold)}
  .prize-label b{color:var(--purple)}
  .prize.two .prize-amount{left:80px;top:8px;font-size:38px;line-height:46px}
  .prize.two .prize-amount small{font-size:20px;vertical-align:12px}
  .prize-brand{position:absolute;left:80px;top:55px;width:112px;text-align:center;font-weight:800;font-size:14px;color:var(--green)}
  .prize-card{position:absolute;left:16px;top:72px;width:180px;text-align:center;font-weight:800;font-size:27px;color:var(--gold)}

  .footer-band{left:0;top:1151px;width:990px;height:49px;background:var(--purple)}
  .contact-label{left:66px;top:1125px;width:428px;height:54px;background:var(--slate);color:#fff;font-weight:700;font-size:22px;line-height:54px;padding-left:33px}
  .contact-mail{left:494px;top:1125px;width:430px;height:54px;background:var(--gold);color:#fff;font-weight:700;font-size:22px;line-height:54px;padding-left:22px;display:flex;align-items:center;gap:10px}
</style>
</head>
<body>
  <div class="abs top-white"></div>

  <svg class="abs hero-art" width="990" height="600" viewBox="0 0 990 600">
    <defs>
      <linearGradient id="classroom" x1="0" y1="0" x2="0" y2="1">
        <stop offset="0" stop-color="#d9d9dc"/>
        <stop offset=".45" stop-color="#b7a6a0"/>
        <stop offset="1" stop-color="#d7b88f"/>
      </linearGradient>
      <linearGradient id="badgeFill" x1="0" y1="0" x2="0" y2="1">
        <stop offset="0" stop-color="#7644ad"/>
        <stop offset="1" stop-color="#4b1a8a"/>
      </linearGradient>
    </defs>
    <path d="M409,0 L560,0 Q470,8 450,60 Z" fill="var(--purple)"/>
    <path d="M870,0 L990,0 L990,60 Q970,10 870,0 Z" fill="var(--purple)"/>
    <path d="M990,400 L990,589 L835,589 Q805,575 790,540 L880,540 Z" fill="var(--purple)"/>
    <path role="img" aria-label="Photo of students seated in a lecture hall" d="M520,0 L990,0 L990,417 L880,540 Q870,551 855,551 L560,551 Q548,551 540,540 L377,290 L448,62 Q462,20 520,0 Z" fill="url(#classroom)"/>
    <polygon points="269,240 424,308 462,460 355,582 183,582 76,460 114,308" fill="url(#badgeFill)" stroke="var(--purple)" stroke-width="4" stroke-linejoin="round"/>
    <polygon points="269,250 416,315 452,459 350,574 188,574 86,459 122,315" fill="none" stroke="#a88bd0" stroke-width="1.2" stroke-linejoin="round"/>
    <polygon points="78,326 475,326 488,402 63,402" fill="var(--gold)"/>
  </svg>

  <div class="abs brand">
    <div class="brand-name">FPX<br>TQRVA</div>
    <div class="brand-tagline">Tessaly Quorum Research Vanguard Alliance</div>
  </div>

  <div class="abs badge-title">MEMBERSHIP</div>
  <div class="abs badge-price">$20</div>
  <div class="abs badge-term">PER YEAR</div>

  <div class="abs benefits-head">MEMBER <span>BENEFITS</span></div>
  <ul class="abs benefits">
    <li><svg viewBox="0 0 14 14"><circle cx="7" cy="7" r="6" fill="none" stroke="#4b1a8a" stroke-width="1.2"/><path d="M4.2,7.2 L6.2,9 L9.8,5" fill="none" stroke="#4b1a8a" stroke-width="1.2"/></svg>Access to exclusive Interdisciplinary world-renowned<br>guest speaker presentations</li>
    <li><svg viewBox="0 0 14 14"><circle cx="7" cy="7" r="6" fill="none" stroke="#4b1a8a" stroke-width="1.2"/><path d="M4.2,7.2 L6.2,9 L9.8,5" fill="none" stroke="#4b1a8a" stroke-width="1.2"/></svg>Mentorship for residencies / Oral Medicine Fellowship<br>for nondental healthcare students</li>
    <li><svg viewBox="0 0 14 14"><circle cx="7" cy="7" r="6" fill="none" stroke="#4b1a8a" stroke-width="1.2"/><path d="M4.2,7.2 L6.2,9 L9.8,5" fill="none" stroke="#4b1a8a" stroke-width="1.2"/></svg>Shadowing opportunities with Oral Medicine Specialist</li>
    <li><svg viewBox="0 0 14 14"><circle cx="7" cy="7" r="6" fill="none" stroke="#4b1a8a" stroke-width="1.2"/><path d="M4.2,7.2 L6.2,9 L9.8,5" fill="none" stroke="#4b1a8a" stroke-width="1.2"/></svg>Participate in research journal club</li>
    <li><svg viewBox="0 0 14 14"><circle cx="7" cy="7" r="6" fill="none" stroke="#4b1a8a" stroke-width="1.2"/><path d="M4.2,7.2 L6.2,9 L9.8,5" fill="none" stroke="#4b1a8a" stroke-width="1.2"/></svg>Clinical Research, Case Reports and Lindqvart<br>Fellowship opportunities</li>
    <li><svg viewBox="0 0 14 14"><circle cx="7" cy="7" r="6" fill="none" stroke="#4b1a8a" stroke-width="1.2"/><path d="M4.2,7.2 L6.2,9 L9.8,5" fill="none" stroke="#4b1a8a" stroke-width="1.2"/></svg>Exclusive Lunch and Learn Invitations</li>
    <li><svg viewBox="0 0 14 14"><circle cx="7" cy="7" r="6" fill="none" stroke="#4b1a8a" stroke-width="1.2"/><path d="M4.2,7.2 L6.2,9 L9.8,5" fill="none" stroke="#4b1a8a" stroke-width="1.2"/></svg>10% Discount to Special Events Sponsored by TQRVA</li>
    <li><svg viewBox="0 0 14 14"><circle cx="7" cy="7" r="6" fill="none" stroke="#4b1a8a" stroke-width="1.2"/><path d="M4.2,7.2 L6.2,9 L9.8,5" fill="none" stroke="#4b1a8a" stroke-width="1.2"/></svg>Enhance your Interdisciplinary resource network</li>
  </ul>

  <div class="abs advisers-head">ORGANIZATION ADVISERS</div>
  <div class="abs portrait one" role="img" aria-label="Portrait photo of Dr. Torvald Penning"></div>
  <div class="abs adviser one">
    <div class="adviser-name">Dr. Torvald Penning</div>
    <div class="adviser-school">FPX School of<br>Dental Medicine</div>
  </div>
  <div class="abs portrait two" role="img" aria-label="Portrait photo of Dr. Felix Ormond"></div>
  <div class="abs adviser two">
    <div class="adviser-name">Dr. Felix Ormond</div>
    <div class="adviser-school">FPX Talwick<br>School of Medicine</div>
  </div>

  <div class="abs raffle"></div>
  <div class="abs raffle-title">RENEW OR JOIN</div>
  <div class="abs raffle-deadline">TQRVA BY AUGUST 30TH</div>
  <div class="abs raffle-note">and be entered in a free raffle<br>for the chance to win one of 3 drawings</div>

  <div class="abs prize one">
    <div class="bow" role="img" aria-label="Gold gift ribbon bow"></div>
    <div class="prize-amount">$50</div>
    <div class="prize-label"><b>PAVEX</b> GIFT CARD</div>
  </div>
  <div class="abs prize two">
    <div class="bow" role="img" aria-label="Gold gift ribbon bow"></div>
    <div class="prize-amount"><small>2X</small>$25</div>
    <div class="prize-brand">BREWMOOR</div>
    <div class="prize-card">GIFT CARD</div>
  </div>

  <div class="abs footer-band"></div>
  <div class="abs contact-label">Contact Milo Banter to Join at</div>
  <div class="abs contact-mail">
    <svg width="24" height="17" viewBox="0 0 24 17"><rect x="1" y="1" width="22" height="15" fill="none" stroke="#fff" stroke-width="1.5"/><path d="M1,1 L12,10 L23,1 M1,16 L9,8 M23,16 L15,8" fill="none" stroke="#fff" stroke-width="1.5"/></svg>
    <span>banmil42@learners.fpx.edu</span>
  </div>
</body>
</html>
```